Business card needed for home based pen making business.

I'm after a business card that's a bit more than an off the shelf card. I do like the idea of a card split horizontal with different colours used. A third colour is to be used for the business name and if need a forth for the other details.

I don't have a logo and will pay extra for one ($150 extra). I mainly make pens and seam rippers (stitch unpicks). The logo may be used for a website in future, as will the colours so please provide the colour codes and font type.

I'd like the business name in an easy to read script font at the top (with logo if you have one) and the other details to the bottom left hand side. I'll leave it up to you to match the script to the font used for the other details.

I'd like to keep a triangular balance to the card so something like a siloet of pot containing pens on the bottom right could be used to balance it out. There my ideas I want to see your.

Business name: Quill & Co
Email address: quillandco@mailbox-example.net
Contact: Trevor
Phone: 0412 555 874
No address is to be used on card.

Target Market(s)

Wide variety of people visiting craft markets. Age range 30+.

Industry/Entity Type

Business

Contact Information for Business Card

Quill & Co

Font styles to use
Script

Colors
f0ecf4
3277b5
3176b5

Requirements
Must have
• Contact: Trevor
• Phone: 0412 555 874
• Email address: quillandco@mailbox-example.net
Nice to have
• An icon and/or graphics depicting pens and seam rippers..
Should not have
• I don't want icon/ graphic to be a crossed pen and seam ripper.

```html
<!DOCTYPE html>
<html lang="en">
<head>
<meta charset="utf-8">
<title>Quill &amp; Co — Business Cards</title>
<link rel="stylesheet" href="https://fonts.googleapis.com/css2?family=Tinos:wght@400;700&display=swap">
<style>
  :root {
    --backdrop: #e8e2d8;
    --paper: #ffffff;
    --accent-red: #e31e24;
    --brand-blue: #0067b1;
    --brand-charcoal: #2b2a29;
    --name-blue: #0a64ad;
    --name-charcoal: #2a2a2a;
    --art-light: #eef0f3;
    --art-mid: #d6dbe2;
  }
  * { box-sizing: border-box; margin: 0; padding: 0; }
  html, body {
    width: 1200px; height: 940px; overflow: hidden;
    background: var(--backdrop);
    font-family: "Tinos", "Times New Roman", serif;
  }
  .stage { position: relative; width: 1200px; height: 940px; }

  .card {
    position: absolute; width: 412px; height: 709px;
    background: var(--paper); overflow: hidden;
    box-shadow: 0 2px 6px rgba(0,0,0,0.18);
  }
  .card--blue { left: 100px; top: 97px; --band: var(--brand-blue); --name: var(--name-blue); }
  .card--charcoal { left: 617px; top: 93px; --band: var(--brand-charcoal); --name: var(--name-charcoal); }

  .card__stripe { position: absolute; left: 0; top: 282px; width: 100%; height: 10px; background: var(--accent-red); }
  .card__base { position: absolute; left: 0; top: 292px; width: 100%; bottom: 0; background: var(--band); }

  .card__brand {
    position: absolute; top: 98px; width: 100%; text-align: center;
    font-weight: 700; font-size: 34px; color: var(--name); letter-spacing: 0.2px;
  }

  .card__art {
    position: absolute; left: 118px; top: 140px; width: 196px; height: 258px;
    background: linear-gradient(180deg, var(--art-light), var(--art-mid));
    border-radius: 4px;
  }

  .card__details {
    position: absolute; top: 447px; width: 100%; text-align: center; color: #fff;
  }
  .card__contact-name { font-weight: 700; font-size: 23px; margin-bottom: 38px; }
  .card__line {
    display: flex; align-items: center; justify-content: center; gap: 6px;
    font-size: 23px; line-height: 29px;
  }
  .card__line svg { flex: none; }
  .card__line--email { font-size: 21px; }
</style>
</head>
<body>
<main class="stage">
  <section class="card card--blue">
    <div class="card__stripe"></div>
    <div class="card__base"></div>
    <h1 class="card__brand">Quill &amp; Co</h1>
    <div class="card__art" role="img" aria-label="Illustration of seam rippers and a pen standing in a pot"></div>
    <div class="card__details">
      <p class="card__contact-name">Trevor</p>
      <p class="card__line">
        <svg width="14" height="18" viewBox="0 0 14 18" aria-hidden="true"><path d="M3 1 L6 4 L4.5 6.5 Q6 11 9 13 L11 11.5 L13.5 14.5 L11 17 Q4 15 1 5 Z" fill="#fff"/></svg>
        <span>0412 555 874</span>
      </p>
      <p class="card__line card__line--email">
        <svg width="22" height="14" viewBox="0 0 22 14" aria-hidden="true"><rect x="1" y="1" width="20" height="12" fill="none" stroke="#fff" stroke-width="1.6"/><path d="M1 1 L11 8 L21 1" fill="none" stroke="#fff" stroke-width="1.6"/></svg>
        <span>quillandco@mailbox-example.net</span>
      </p>
    </div>
  </section>

  <section class="card card--charcoal">
    <div class="card__stripe"></div>
    <div class="card__base"></div>
    <h1 class="card__brand">Quill &amp; Co</h1>
    <div class="card__art" role="img" aria-label="Illustration of seam rippers and a pen standing in a pot"></div>
    <div class="card__details">
      <p class="card__contact-name">Trevor</p>
      <p class="card__line">
        <svg width="14" height="18" viewBox="0 0 14 18" aria-hidden="true"><path d="M3 1 L6 4 L4.5 6.5 Q6 11 9 13 L11 11.5 L13.5 14.5 L11 17 Q4 15 1 5 Z" fill="#fff"/></svg>
        <span>0412 555 874</span>
      </p>
      <p class="card__line card__line--email">
        <svg width="22" height="14" viewBox="0 0 22 14" aria-hidden="true"><rect x="1" y="1" width="20" height="12" fill="none" stroke="#fff" stroke-width="1.6"/><path d="M1 1 L11 8 L21 1" fill="none" stroke="#fff" stroke-width="1.6"/></svg>
        <span>quillandco@mailbox-example.net</span>
      </p>
    </div>
  </section>
</main>
</body>
</html>
```